Professional Business Cards

We need a nice looking, profession and modern business card for our new company. Our logo is attatched

Target Market(s)

Young Professionals

Industry/Entity Type

Financial

Contact Information for Business Card

FRONT

Morvane Tally Pty Ltd
Level 22, Halden Court, 48 Wirrapool St
Sydney NSW 2000
ABN : 57 304 918 226

Derek Wallis - Chief Operations Officer
P : 02 7153 2819
M: 0418 395 207
derek@morvanetally,com

BACK

- Cryptocurrency Exchange Services
- Cryptocurrency Mining Operations
- Cryptocurrency Investment Fund Offering

Font styles to use
Sans Serif

Colors
0255a3
9d9d9d

```html
<!DOCTYPE html>
<html lang="en">
<head>
<meta charset="utf-8">
<title>Morvane Tally – Business Cards</title>
<link rel="stylesheet" href="https://fonts.googleapis.com/css2?family=Fira+Sans+Condensed:wght@400;500;600;700&display=swap">
<style>
  :root {
    --brand-blue: #0255a3;
    --brand-blue-deep: #0a4c92;
    --brand-grey: #9d9d9d;
    --mark-grey: #6a6a6a;
    --text-grey: #4a4a4a;
    --card-white: #f2f2f2;
    --stage: #c8c8c8;
    --line-blue: #3a8ae0;
  }
  * { margin: 0; padding: 0; box-sizing: border-box; }
  html, body {
    width: 1200px; height: 576px; overflow: hidden;
    background: var(--stage);
    font-family: "Fira Sans Condensed", Arial, sans-serif;
  }
  .stage { position: relative; width: 1200px; height: 576px; }

  .card {
    position: absolute; top: 138px;
    width: 484px; height: 294px;
    overflow: hidden;
  }

  /* Back of card: services */
  .card--back {
    left: 82px;
    background: linear-gradient(180deg, var(--brand-blue) 0%, var(--brand-blue-deep) 100%);
    color: #fff;
  }
  .card--back .wordmark {
    position: absolute; left: 0; right: 0; top: 82px;
    text-align: center;
    font-size: 52px; font-weight: 700; letter-spacing: 2px; line-height: 1;
    color: #fff;
  }
  .service-rule {
    position: absolute; left: 0; right: 0; height: 1px;
    background: var(--line-blue); opacity: .55;
  }
  .services { position: absolute; left: 0; right: 0; top: 218px; list-style: none; }
  .services li {
    position: relative; height: 15.5px; line-height: 15.5px;
    text-align: center; font-size: 12.5px; font-weight: 500;
  }
  .services li span {
    position: relative; padding: 0 14px;
    background: linear-gradient(90deg, transparent 0, var(--brand-blue-deep) 12px, var(--brand-blue-deep) calc(100% - 12px), transparent 100%);
  }
  .services li span::before,
  .services li span::after {
    content: ""; position: absolute; top: 5px;
    width: 5px; height: 5px;
    border: 1px solid var(--line-blue);
    transform: rotate(45deg);
  }
  .services li span::before { left: 2px; }
  .services li span::after { right: 2px; }

  /* Front of card: contact */
  .card--front { left: 602px; background: var(--card-white); }
  .card--front .wordmark {
    position: absolute; left: 18px; top: 20px;
    font-size: 38px; font-weight: 700; letter-spacing: 1px; line-height: 1;
    color: var(--brand-blue);
  }
  .brand-square {
    position: absolute; left: 270px; top: 60px;
    width: 176px; height: 176px;
    background: var(--mark-grey);
  }
  .person { position: absolute; left: 18px; top: 110px; }
  .person__name { font-size: 21px; font-weight: 700; letter-spacing: 1px; line-height: 1.1; color: var(--brand-blue); }
  .person__role { font-size: 10.5px; font-weight: 500; color: var(--text-grey); margin-top: 1px; }

  .contact { position: absolute; left: 18px; top: 163px; list-style: none; }
  .contact li {
    display: flex; align-items: center; gap: 6px;
    height: 15.5px; font-size: 11.5px; color: var(--text-grey);
  }
  .contact svg { width: 10px; height: 10px; fill: var(--brand-blue); flex: none; }
  .contact .accent { color: var(--brand-blue); }

  .address {
    position: absolute; left: 18px; top: 243px;
    font-size: 11.5px; line-height: 16px; color: var(--text-grey); font-style: normal;
  }
</style>
</head>
<body>
<main class="stage">

  <section class="card card--back" aria-label="Card back">
    <div class="wordmark">MORVANE TALLY</div>
    <div class="service-rule" style="top:226px"></div>
    <div class="service-rule" style="top:241px"></div>
    <div class="service-rule" style="top:257px"></div>
    <ul class="services">
      <li><span>Cryptocurrency Exchange Services</span></li>
      <li><span>Cryptocurrency Mining Operations</span></li>
      <li><span>Cryptocurrency Investment Fund Offering</span></li>
    </ul>
  </section>

  <section class="card card--front" aria-label="Card front">
    <div class="wordmark">MORVANE TALLY</div>

    <div class="brand-square" role="img" aria-label="Brand mark area"></div>

    <div class="person">
      <div class="person__name">DEREK WALLIS</div>
      <div class="person__role">Chief Operations Officer</div>
    </div>

    <ul class="contact">
      <li>
        <svg viewBox="0 0 10 10" aria-hidden="true"><path d="M0 4c0-2 2-3 5-3s5 1 5 3v1H7V4H3v1H0z M2 5h6l1 4H1z"/></svg>
        02 7153 2819
      </li>
      <li>
        <svg viewBox="0 0 10 10" aria-hidden="true"><path d="M2.5 0h5a1 1 0 0 1 1 1v8a1 1 0 0 1-1 1h-5a1 1 0 0 1-1-1V1a1 1 0 0 1 1-1zm.5 1.5v6h4v-6z"/></svg>
        0418 395 207
      </li>
      <li>
        <svg viewBox="0 0 10 10" aria-hidden="true"><path d="M0 2h10v.6L5 6 0 2.6z M0 3.6l5 3.4 5-3.4V8H0z"/></svg>
        derek@morvanetally,com
      </li>
      <li>
        <svg viewBox="0 0 10 10" aria-hidden="true"><path d="M5 0a5 5 0 1 0 0 10A5 5 0 0 0 5 0zm0 1c.8.8 1.3 2.3 1.4 3.5H3.6C3.7 3.3 4.2 1.8 5 1zM1.1 4.5a4 4 0 0 1 1.8-3A7 7 0 0 0 2.6 4.5zm0 1h1.5c.1 1.2.4 2.3.9 3a4 4 0 0 1-2.4-3zm2.5 0h2.8C6.3 6.7 5.8 8.2 5 9c-.8-.8-1.3-2.3-1.4-3.5zm3.8 0h1.5a4 4 0 0 1-2.4 3c.5-.7.8-1.8.9-3zm0-1a7 7 0 0 0-.3-3 4 4 0 0 1 1.8 3z"/></svg>
        <span>www.<span class="accent">morvanetally</span>.com</span>
      </li>
      <li>
        <svg viewBox="0 0 10 10" aria-hidden="true"><path d="M3 0h1.2l-.4 3h2.4l.4-3h1.2l-.4 3H9v1.2H7.2l-.3 1.6H9V7H6.7l-.4 3H5.1l.4-3H3.1l-.4 3H1.5l.4-3H0V5.8h2.1l.3-1.6H0V3h2.6zm.6 4.2-.3 1.6h2.4L6 4.2z"/></svg>
        <span><span class="accent">ABN</span> : 57 304 918 226</span>
      </li>
    </ul>

    <address class="address">
      Level 22, Halden Court, 48<br>
      Wirrapool St Sydney NSW 2000
    </address>
  </section>

</main>
</body>
</html>
```